Cycling Group adventures - weekly cycling with Pedal Southland Coach for health and fitness

An A3 poster, like a flyer for information about a new cycling group. Lots of info on the poster so designed to be read close up and not needing to get attention from a long way off. All the info, yes there is a lot, is on the Word document attached. My colours are blue RGB 83, 108, 255 and orange 226, 83, 3.
There are three sections of info on the Word document the first is the most important.
The market is affluent and middle-aged.
So nothing wild or shouty. Nice, sophisticated, peaceful designs.
Photos really are background to the words. (I think I've accidentally downloaded some twice although I thought they were deleted.)

Industry/Entity Type

Health And Wellness

Font styles to use
Sans Serif

Requirements
Must have
• Clear font
Should not have
• Jazzy colours, lots of bubbles, flashy things or anything that looks like an advert for cheap jewellery/perfume/used cars.

```html
<!DOCTYPE html>
<html lang="en">
<head>
<meta charset="utf-8">
<title>Join us – weekly cycling sessions</title>
<link rel="stylesheet" href="https://fonts.googleapis.com/css2?family=Oswald:wght@500&family=Source+Sans+3:wght@300;400;600;700&display=swap">
<style>
  :root {
    --orange: #e25303;
    --blue: #536cff;
    --green: #6d8f3e;
    --green-dark: #557a2c;
    --ink: #222;
    --ink-soft: #444;
    --panel: #e9eaec;
    --rule: #9aa0a8;
    --label-bg: #e8ecf3;
    --white: #fff;
  }
  * { box-sizing: border-box; margin: 0; padding: 0; }
  html, body { width: 849px; height: 1200px; overflow: hidden; background: var(--white); }
  body { position: relative; font-family: "Source Sans 3", Arial, sans-serif; color: var(--ink); }

  .hero { position: absolute; left: 0; top: 0; width: 849px; height: 400px; overflow: hidden; }
  .hero-photo { position: absolute; inset: 0;
    background: linear-gradient(90deg, #4c5a3a 0%, #8a6f6c 18%, #c97b83 32%, #9b8d86 48%, #6b7d4b 62%, rgba(109,143,62,0.9) 78%, var(--green-dark) 100%); }
  .hero-title { position: absolute; left: 544px; top: 22px; font-family: "Oswald", "Arial Narrow", sans-serif; font-weight: 500; font-size: 100px; line-height: 1; color: var(--white); letter-spacing: 1px; }
  .info-box { position: absolute; left: 498px; width: 314px; background: var(--white); border-radius: 0 22px 22px 0; }
  .info-box.where { top: 133px; height: 63px; }
  .info-box.when { top: 209px; height: 64px; }
  .info-box.whom { top: 287px; height: 64px; }
  .tab { position: absolute; left: 492px; background: var(--orange); color: var(--white); font-weight: 700; font-size: 15px; padding: 1px 7px 2px; border-radius: 0 8px 0 0; }
  .tab.where { top: 128px; } .tab.when { top: 204px; } .tab.whom { top: 283px; }
  .when-row { position: absolute; left: 68px; font-weight: 600; font-size: 15px; }
  .when-row.day { top: 10px; } .when-row.date { top: 31px; }
  .when-line { position: absolute; left: 110px; width: 180px; border-bottom: 1px dashed #bbb; height: 1px; }
  .when-line.day { top: 24px; } .when-line.date { top: 46px; }
  .date-tick { position: absolute; top: 29px; width: 2px; height: 17px; background: #333; }
  .when-note { position: absolute; left: 70px; top: 50px; font-size: 10px; letter-spacing: .4px; }
  .whom-text { position: absolute; left: 68px; top: 12px; font-size: 27px; letter-spacing: .3px; }
  .booking { position: absolute; left: 491px; top: 358px; color: var(--white); font-size: 13.5px; font-weight: 600; }
  .booking b { font-weight: 700; }

  .coach { position: absolute; left: 36px; top: 436px; width: 777px; height: 327px; background: linear-gradient(180deg, #eef0f2 0%, #e2e4e7 100%); }
  .coach-bio { position: absolute; left: 21px; top: 19px; width: 310px; font-weight: 300; font-size: 18px; line-height: 30.3px; color: #333; }
  .coach-photo { position: absolute; left: 336px; top: 10px; width: 229px; height: 317px; background: linear-gradient(180deg, #d9c1ad 0%, #c9a993 35%, #5d86c9 60%, #3f6dc2 100%); border-radius: 90px 90px 0 0; }
  .contact { position: absolute; left: 620px; width: 240px; margin-left: -120px; text-align: center; }
  .contact-lead { top: 26px; font-size: 19px; line-height: 21px; color: #222; }
  .contact-phone { top: 70px; font-size: 31px; letter-spacing: 1px; color: #111; }
  .contact-or { top: 110px; font-size: 10px; }
  .contact-web { top: 128px; font-size: 17px; font-weight: 700; }
  .price { top: 206px; font-weight: 300; font-size: 70px; line-height: 1; color: #111; }
  .price-note { top: 287px; font-size: 11px; color: #555; }

  .faq { position: absolute; left: 36px; top: 799px; width: 777px; border-collapse: collapse; font-size: 11px; }
  .faq td { border-top: 1px solid var(--rule); padding: 4px 6px 0; vertical-align: top; line-height: 13px; }
  .faq tr:last-child td { border-bottom: 1px solid var(--rule); }
  .faq .q { width: 170px; background: var(--label-bg); color: var(--ink); }
  .faq .a { color: var(--ink-soft); font-weight: 300; }
  .faq.main td { height: 22.4px; }
  .faq.main tr.tall td { height: 36px; }
  .options-head { position: absolute; left: 41px; top: 1070px; color: var(--orange); font-size: 12px; font-weight: 600; }
  .faq.options { top: 1085px; }
  .faq.options .q { width: 379px; }
  .faq.options td { height: 22px; }
  .faq.options tr.tall td { height: 34px; }
</style>
</head>
<body>
  <header class="hero">
    <div class="hero-photo" role="img" aria-label="Photo of three smiling women in helmets standing with their bikes on a leafy path"></div>
    <h1 class="hero-title">Join us</h1>

    <span class="tab where">Where</span>
    <div class="info-box where"></div>

    <span class="tab when">When</span>
    <div class="info-box when">
      <span class="when-row day">Day</span>
      <span class="when-line day"></span>
      <span class="when-row date">Date</span>
      <span class="when-line date"></span>
      <span class="date-tick" style="left:172px"></span>
      <span class="date-tick" style="left:216px"></span>
      <span class="when-note">Weekly 60 min (or so) sessions for 5 weeks.</span>
    </div>

    <span class="tab whom">Whome</span>
    <div class="info-box whom"><span class="whom-text">Up to 7 participants</span></div>

    <p class="booking"><b>Booking essential?</b> Yes, for purposes of insurance.</p>
  </header>

  <section class="coach">
    <p class="coach-bio">Daniel Hartley, Pedal Southland Accredited Coach, coach to the Junior Emerging Talent squad of Qld, ride leader of Pedal Southland’s Ride Together and Open Road programmes and has an Exercise Physiology and Biomechanics degree tutored by Ian Marlow who co-founded the Northgate Sports Medical Centre. Daniel can talk whilst cycling uphill but will limit this to useful things.</p>
    <div class="coach-photo" role="img" aria-label="Photo of the coach in a blue and white cycling jersey"></div>
    <p class="contact contact-lead">For Registration and enquiry<br>Phone my number</p>
    <p class="contact contact-phone">0400 555 218</p>
    <p class="contact contact-or">or</p>
    <p class="contact contact-web">www.wheelhouseride.com.au</p>
    <p class="contact price">$129</p>
    <p class="contact price-note">for the 5 weeks</p>
  </section>

  <table class="faq main">
    <tr><td class="q">Women and men?</td><td class="a">Either/both though this time-frame is female dominated.</td></tr>
    <tr><td class="q">Is it competitive?</td><td class="a">No. No it isn’t</td></tr>
    <tr><td class="q">Might I get left behind?</td><td class="a">No. No you won’t.</td></tr>
    <tr class="tall"><td class="q">Clothing?</td><td class="a">Close fitting sporting clothing is fine if you are not a ‘lycra’ wearer. Full pro kit welcomed too if you like that.<br>So long as it’s comfortable and won’t get caught in moving parts. Helmet? Australian law so it’s essential.</td></tr>
    <tr class="tall"><td class="q">Bike?</td><td class="a">All types welcomed. If you are on a classic beach cruiser or town bike weighing 20kg it does make it harder.<br>I’ll help make sure your bike fits you.</td></tr>
    <tr class="tall"><td class="q">Ability level?</td><td class="a">Aimed at people who can ride a bike, including moderate inclines, but wouldn’t currently have the confidence to do<br>a 20km ride. Also aimed at people who may be able to do 20km but would like it to be easier.</td></tr>
    <tr><td class="q">Will it be a mixed ability?</td><td class="a">Always. I adapt to this in every session I do as needs demand.</td></tr>
    <tr class="tall"><td class="q">Do we have coffee afterwards?</td><td class="a">If you like? It is fairly traditional. Also it is a good time to ask if you enjoyed it, achieved in the session what you wanted<br>and what you’d like to work on next, whatever that may be.</td></tr>
    <tr><td class="q">Now what?</td><td class="a">Booking by phone is the best way.</td></tr>
  </table>

  <h2 class="options-head">Some Other Options</h2>
  <table class="faq options">
    <tr><td class="q">I’d like a different day and time</td><td class="a">Give me a ring we’ll work out a plan</td></tr>
    <tr><td class="q">I ride regularly and can do 55km in 2 hours and want to be even quicker</td><td class="a">This is good, give me a ring we’ll work out a plan.</td></tr>
    <tr class="tall"><td class="q">I, however, can hardly ride at all and haven’t been on a bike in a while</td><td class="a">I also present Basics from Pedal Southland. Call for details or see the Pedal Southland website for details. Give me a ring and we’ll work out a plan.</td></tr>
  </table>
</body>
</html>
```